Swimming pool service business postcard redesign

We need a fresh post card design for our pool service business based in San Diego called Tide Sweepers. We are a family based, local residential pool cleaning and maintenance company. we need an offer to stand out, our logo, our colors, etc on a 5.5x8 inch full color post card.

```html
<!DOCTYPE html>
<html lang="en">
<head>
<meta charset="utf-8">
<title>Tide Sweepers – Postcard</title>
<link rel="stylesheet" href="https://fonts.googleapis.com/css2?family=Oswald:wght@500;600;700&family=Anton&family=Poppins:wght@400;600;700;800&family=Kaushan+Script&display=swap">
<style>
:root{
  --stage:#a8a8a8;
  --navy:#0d2a5e;
  --navy-deep:#0a2352;
  --blue:#1464b4;
  --orange:#f05a14;
  --white:#ffffff;
  --muted:#b9c3d3;
  --ink:#1b2230;
  --rule:#c9c9c9;
}
*{margin:0;padding:0;box-sizing:border-box}
html,body{width:1015px;height:1200px;overflow:hidden}
body{background:var(--stage);position:relative;font-family:'Poppins',sans-serif}

.card{position:absolute;width:677px;height:465px;overflow:hidden;box-shadow:0 4px 12px rgba(0,0,0,.35)}
.card-front{left:161px;top:121px;background:linear-gradient(180deg,#d7ecfa 0%,#e7f3fb 55%,#f7fbfe 100%)}
.card-back{left:166px;top:630px;background:var(--white)}
.abs{position:absolute}

/* front */
.splash{left:-40px;top:40px;width:560px;height:340px;background:radial-gradient(ellipse closest-side at 50% 50%,#1e6fc0 0%,#4b98d8 45%,rgba(160,205,238,.6) 75%,rgba(230,243,251,0) 100%)}
.mascot{left:118px;top:66px;width:190px;height:132px;border-radius:14px;background:linear-gradient(160deg,#f07a3a,#2b62b0)}
.tagline-top{left:70px;top:22px;font-family:'Oswald',sans-serif;font-weight:500;font-size:11px;color:var(--navy);transform:rotate(-6deg)}
.tagline-script{left:44px;top:42px;font-family:'Kaushan Script',cursive;font-size:15px;color:var(--navy);transform:rotate(-6deg)}
.brand{left:40px;top:196px;font-family:'Anton',sans-serif;font-size:44px;line-height:.95;color:var(--white)}
.brand-sub{left:130px;top:292px;background:var(--orange);color:var(--white);font-family:'Oswald',sans-serif;font-weight:600;font-size:10px;letter-spacing:2px;padding:2px 10px}

.head-1{left:380px;top:32px;font-family:'Anton',sans-serif;font-size:28px;line-height:1;color:var(--ink);letter-spacing:1px;transform:rotate(-3deg)}
.head-2{left:376px;top:60px;font-family:'Anton',sans-serif;font-size:66px;line-height:1;color:var(--navy);letter-spacing:4px;transform:rotate(-3deg)}
.head-3{left:380px;top:128px;font-family:'Oswald',sans-serif;font-weight:700;font-size:20px;line-height:1.1;color:var(--orange);transform:rotate(-3deg)}

.offer{left:486px;top:150px;width:183px;height:280px}
.offer svg{position:absolute;inset:0}
.offer-ribbon{left:10px;top:4px;background:var(--navy);color:var(--white);font-family:'Oswald',sans-serif;font-weight:600;font-size:11px;padding:3px 12px;transform:rotate(-3deg)}
.offer-lead{left:0;width:183px;top:36px;text-align:center;font-family:'Oswald',sans-serif;font-weight:600;font-size:15px;line-height:1.05;color:var(--white);transform:rotate(-3deg)}
.offer-price{left:0;width:183px;top:66px;text-align:center;font-family:'Anton',sans-serif;font-size:62px;line-height:1;color:var(--white);transform:rotate(-3deg)}
.offer-fee{left:34px;top:138px;background:var(--navy);color:var(--white);font-family:'Oswald',sans-serif;font-weight:600;font-size:10px;padding:2px 9px;border-radius:3px;transform:rotate(-3deg)}
.offer-list{left:28px;top:160px;list-style:none;transform:rotate(-3deg)}
.offer-list li{display:flex;align-items:center;gap:5px;font-family:'Oswald',sans-serif;font-weight:500;font-size:10.5px;color:var(--white);height:15px}
.offer-list svg{position:static;width:11px;height:11px}
.offer-note{left:52px;top:222px;font-family:'Kaushan Script',cursive;font-size:12px;color:var(--white);white-space:nowrap;transform:rotate(-10deg)}

.features{left:18px;top:345px;display:flex}
.feature{width:78px;text-align:center;font-size:6.5px;letter-spacing:.5px;line-height:1.3;color:var(--navy);border-right:1px solid #d4a088}
.feature:last-child{border-right:none}
.feature svg{width:24px;height:24px;display:block;margin:0 auto 4px}

.contact-bar{left:0;top:402px;width:677px;height:63px;background:var(--navy)}
.cbar-icon{width:34px;height:34px;border-radius:50%;background:var(--orange);top:14px;display:flex;align-items:center;justify-content:center}
.cbar-icon svg{width:19px;height:19px}
.cbar-label{font-family:'Oswald',sans-serif;font-weight:600;font-size:10px;color:var(--orange);top:10px}
.cbar-value{font-family:'Oswald',sans-serif;font-weight:700;font-size:25px;color:var(--white);top:20px;line-height:1.2}
.cbar-rule{top:12px;width:1px;height:38px;background:#5c719a}
.cbar-address{left:547px;top:16px;font-family:'Oswald',sans-serif;font-weight:500;font-size:11.5px;line-height:1.35;color:var(--white)}

/* back */
.services-panel{left:0;top:0;width:362px;height:465px;background:var(--navy-deep)}
.services-title{left:0;width:352px;top:13px;text-align:center;font-weight:700;font-size:16px;color:var(--muted)}
.service{width:110px;text-align:center}
.service-icon{width:50px;height:50px;border:1.5px solid var(--orange);border-radius:50%;margin:0 auto;display:flex;align-items:center;justify-content:center}
.service-icon svg{width:26px;height:26px}
.service-name{margin-top:8px;font-weight:800;font-style:italic;font-size:11px;line-height:1.2;color:var(--orange)}
.service-desc{margin:6px auto 0;width:100px;font-size:8.3px;line-height:1.38;color:var(--muted)}
.col-rule{top:49px;width:1px;height:150px;background:#3c5585}
.extra-desc{left:100px;width:112px;top:212px;text-align:center;font-size:8.3px;line-height:1.42;color:var(--muted)}
.callout{left:33px;top:290px;width:180px;height:42px;border-radius:10px;background:var(--orange);text-align:center;color:var(--white)}
.callout-phone{font-weight:700;font-size:21px;line-height:1.2;padding-top:1px}
.callout-web{font-size:12px;line-height:1}
.callout-tail{left:200px;top:305px}
.water-back{left:362px;top:345px;width:315px;height:120px;background:linear-gradient(180deg,rgba(255,255,255,0) 0%,rgba(120,185,235,.55) 40%,#2a7bc8 100%)}
.water-left{left:0;top:400px;width:362px;height:65px;background:linear-gradient(180deg,rgba(42,123,200,0) 0%,#2a7bc8 100%)}
.truck{left:2px;top:340px;width:358px;height:122px;border-radius:18px 40px 10px 10px;background:linear-gradient(90deg,#e8542a 0%,#e98a55 30%,#2f76c2 65%,#1a4f96 100%)}
.mascot-back{left:232px;top:256px;width:128px;height:84px;border-radius:12px;background:linear-gradient(160deg,#f07a3a,#2b62b0 75%)}
.stamp{left:549px;top:44px;width:82px;height:82px;border:1px solid #9a9a9a}
.to-label{left:379px;top:172px;font-weight:800;font-size:13px;color:#000}
.address-line{left:378px;width:252px;height:1px;background:var(--rule)}
</style>
</head>
<body>

<section class="card card-front">
  <div class="abs splash" role="img" aria-label="Blue water splash with bubbles"></div>
  <div class="abs mascot" role="img" aria-label="Cartoon pool technician holding a skimmer net and giving a thumbs up"></div>
  <p class="abs tagline-top">Reliable. Local. Family Owned.</p>
  <p class="abs tagline-script">Proudly Serving San Diego Homes!</p>
  <p class="abs brand">TIDE<br>SWEEPERS</p>
  <p class="abs brand-sub">POOL &amp; SPA SERVICE</p>

  <h1 class="abs head-1">CRYSTAL CLEAR</h1>
  <p class="abs head-2">POOLS</p>
  <p class="abs head-3">WITHOUT THE HASSLE!</p>

  <div class="abs offer">
    <svg viewBox="0 0 183 280" aria-hidden="true">
      <path d="M10 24 Q10 14 20 14 H168 Q178 14 178 24 V222 Q178 236 162 244 L100 276 Q92 280 84 276 L24 244 Q8 236 8 222 Z" fill="#fff"/>
      <path d="M16 28 Q16 20 24 20 H164 Q172 20 172 28 V220 Q172 232 158 239 L98 270 Q92 273 86 270 L28 239 Q14 232 14 220 Z" fill="var(--orange)"/>
    </svg>
    <p class="abs offer-ribbon">NEW CUSTOMER SPECIAL</p>
    <p class="abs offer-lead">START YOUR<br>SERVICE FOR ONLY</p>
    <p class="abs offer-price">$85</p>
    <p class="abs offer-fee">INITIAL START-UP FEE</p>
    <ul class="abs offer-list">
      <li><svg viewBox="0 0 12 12"><circle cx="6" cy="6" r="6" fill="#fff"/><path d="M3.3 6.2l1.8 1.8 3.6-3.8" stroke="var(--orange)" stroke-width="1.6" fill="none"/></svg>Equipment Inspection</li>
      <li><svg viewBox="0 0 12 12"><circle cx="6" cy="6" r="6" fill="#fff"/><path d="M3.3 6.2l1.8 1.8 3.6-3.8" stroke="var(--orange)" stroke-width="1.6" fill="none"/></svg>Water Analysis</li>
      <li><svg viewBox="0 0 12 12"><circle cx="6" cy="6" r="6" fill="#fff"/><path d="M3.3 6.2l1.8 1.8 3.6-3.8" stroke="var(--orange)" stroke-width="1.6" fill="none"/></svg>Filter Assessment</li>
      <li><svg viewBox="0 0 12 12"><circle cx="6" cy="6" r="6" fill="#fff"/><path d="M3.3 6.2l1.8 1.8 3.6-3.8" stroke="var(--orange)" stroke-width="1.6" fill="none"/></svg>Service Setup</li>
    </ul>
    <p class="abs offer-note">Mention this card!</p>
  </div>

  <div class="abs features">
    <div class="feature"><svg viewBox="0 0 24 24" fill="none" stroke="var(--navy)" stroke-width="1.5"><path d="M12 2l8 3v6c0 5-3.5 9-8 11-4.5-2-8-6-8-11V5z"/><path d="M8.5 12l2.5 2.5 4.5-5"/></svg>RELIABLE &amp;<br>PROFESSIONAL</div>
    <div class="feature"><svg viewBox="0 0 24 24" fill="none" stroke="var(--navy)" stroke-width="1.3"><path d="M10 4l1.5 5.5L17 11l-5.5 1.5L10 18l-1.5-5.5L3 11l5.5-1.5z"/><path d="M18 3v4M16 5h4M18 17v4M16 19h4"/></svg>CRYSTAL<br>CLEAR RESULTS</div>
    <div class="feature"><svg viewBox="0 0 24 24" fill="var(--navy)"><path d="M12 3l10 9h-3v9h-5v-6h-4v6H5v-9H2z"/></svg>LOCALLY OWNED<br>&amp; FAMILY BASED</div>
    <div class="feature"><svg viewBox="0 0 24 24" fill="none" stroke="var(--navy)" stroke-width="1.5"><path d="M12 22s7-7.5 7-13a7 7 0 0 0-14 0c0 5.5 7 13 7 13z"/><circle cx="12" cy="9" r="2.5"/></svg>SERVING SAN<br>DIEGO HOMES</div>
  </div>

  <div class="abs contact-bar">
    <div class="abs cbar-icon" style="left:19px"><svg viewBox="0 0 24 24" fill="#fff"><path d="M6.6 10.8a15.1 15.1 0 0 0 6.6 6.6l2.2-2.2a1 1 0 0 1 1-.25 11.4 11.4 0 0 0 3.6.57 1 1 0 0 1 1 1V20a1 1 0 0 1-1 1A17 17 0 0 1 3 4a1 1 0 0 1 1-1h3.5a1 1 0 0 1 1 1c0 1.25.2 2.45.57 3.6a1 1 0 0 1-.25 1z"/></svg></div>
    <p class="abs cbar-label" style="left:62px">CALL OR TEXT TODAY!</p>
    <p class="abs cbar-value" style="left:60px">619-555-0148</p>
    <div class="abs cbar-rule" style="left:253px"></div>
    <div class="abs cbar-icon" style="left:271px"><svg viewBox="0 0 24 24" fill="none" stroke="#fff" stroke-width="1.5"><circle cx="12" cy="12" r="9"/><path d="M3 12h18M12 3c3 3 3 15 0 18M12 3c-3 3-3 15 0 18"/></svg></div>
    <p class="abs cbar-label" style="left:314px">VISIT US ONLINE</p>
    <p class="abs cbar-value" style="left:313px;font-size:23px">TideSweepers.com</p>
    <div class="abs cbar-rule" style="left:486px"></div>
    <div class="abs cbar-icon" style="left:503px"><svg viewBox="0 0 24 24" fill="#fff"><path d="M12 22s7-7.5 7-13a7 7 0 0 0-14 0c0 5.5 7 13 7 13z"/><circle cx="12" cy="9" r="2.5" fill="var(--orange)"/></svg></div>
    <p class="abs cbar-address">1480 Harbor Crest Way<br>San Diego, CA 92123</p>
  </div>
</section>

<section class="card card-back">
  <div class="abs water-back" role="img" aria-label="Blue water wave with bubbles"></div>
  <div class="abs services-panel"></div>
  <div class="abs water-left" role="img" aria-label="Blue water splash under the truck"></div>
  <h2 class="abs services-title">OUR SERVICES</h2>

  <div class="abs service" style="left:12px;top:47px">
    <div class="service-icon"><svg viewBox="0 0 24 24" fill="var(--blue)"><path d="M12 2C9 7 6 10.5 6 14.5a6 6 0 0 0 12 0C18 10.5 15 7 12 2z"/></svg></div>
    <p class="service-name">BASIC<br>SERVICE</p>
    <p class="service-desc">Two visits per month. Diagnostic testing and adjustment for chlorine, pH, and complete water balance</p>
  </div>
  <div class="abs col-rule" style="left:123px"></div>
  <div class="abs service" style="left:124px;top:47px">
    <div class="service-icon"><svg viewBox="0 0 24 24" fill="none" stroke="var(--blue)" stroke-width="1.5"><circle cx="16" cy="8" r="2"/><path d="M5 13l5-5 4 3-3 3M3 17c2-1.5 4-1.5 6 0s4 1.5 6 0 4-1.5 6 0M3 21c2-1.5 4-1.5 6 0s4 1.5 6 0 4-1.5 6 0"/></svg></div>
    <p class="service-name">BASIC PLUS<br>SERVICE</p>
    <p class="service-desc">Include Basic Service, plus quarterly filter cleaning and an equipment evaluation</p>
  </div>
  <div class="abs col-rule" style="left:236px"></div>
  <div class="abs service" style="left:237px;top:47px">
    <div class="service-icon"><svg viewBox="0 0 24 24" fill="none" stroke="var(--blue)" stroke-width="1.5"><path d="M8 16V5a2 2 0 0 1 4 0M16 16V5a2 2 0 0 1 4 0M8 8h8M8 12h8M3 18c2-1.5 4-1.5 6 0s4 1.5 6 0 4-1.5 6 0M3 21c2-1.5 4-1.5 6 0s4 1.5 6 0 4-1.5 6 0"/></svg></div>
    <p class="service-name">FULL<br>SERVICE</p>
    <p class="service-desc">No less than four visits per month. Chemical testing and balance, cleaning, brushing, emptying and filter cleaning</p>
  </div>

  <div class="abs service" style="left:9px;top:195px">
    <div class="service-icon"><svg viewBox="0 0 24 24" fill="none" stroke="var(--blue)" stroke-width="1.3"><path d="M8 8l1.2 4 4 1.2-4 1.2L8 18.4l-1.2-4-4-1.2 4-1.2zM17 3l.8 2.5 2.5.8-2.5.8L17 9.6l-.8-2.5-2.5-.8 2.5-.8zM15 14l.8 2.5 2.5.8-2.5.8-.8 2.5-.8-2.5-2.5-.8 2.5-.8z"/></svg></div>
    <p class="service-name">EXTRA FULL<br>SERVICE</p>
  </div>
  <p class="abs extra-desc">Recommended for pools prone to heavy debris, Includes all Full Service Offerings, with six visits per month.</p>

  <div class="abs truck" role="img" aria-label="Branded service pickup truck wrapped in orange and blue"></div>
  <div class="abs mascot-back" role="img" aria-label="Cartoon pool technician holding a skimmer net over his shoulder"></div>

  <svg class="abs callout-tail" width="40" height="30" viewBox="0 0 40 30" aria-hidden="true"><path d="M0 0 L12 0 L40 28 Z" fill="var(--orange)"/></svg>
  <div class="abs callout">
    <p class="callout-phone">619-555-0148</p>
    <p class="callout-web">www.tidesweepers.com</p>
  </div>

  <div class="abs stamp"></div>
  <p class="abs to-label">TO</p>
  <div class="abs address-line" style="top:222px"></div>
  <div class="abs address-line" style="top:262px"></div>
  <div class="abs address-line" style="top:298px"></div>
  <div class="abs address-line" style="top:340px"></div>
</section>

</body>
</html>
```